In need of a Wordpress website for a Water Sports Rental Company!

We are starting a new venture that provides a variety of rental equipment in the Cayman Islands. We are in need of a website where guests are able to book their rental gear during their stay in Cayman. We will also have an interactive map where guests can learn about off the beaten path activities to explore in here Cayman.

Our target market is middle/upper class, so we need a website that appeals to this group. We need our website to be clean, simple and easy to navigate. We need it to be highly visual and modern. We like the idea of the website having a tropical feel to it, we are very open to creative ideas that reflects this!

Must be designed in WordPress using the Quelmira template I’ve provided.

You will find all instructions & the photos I want to use for this website on the following vaultra account:
- www.vaultra.com
- Username: fun@marlettoboats.com
- Password: lantern4

All of the photos will need to be resized accordingly to be as small as possible without loosing resolution.

These are the tabs that will be used:
- Home Page
- Adventure Map
- Rental Gear
- Tours
- Photo Gallery
- Contact Us

Home Page
- You will find all the text and instructions for the home page in the word document named ‘Home Page’.

Adventure Map
- You will find all the text and instructions for the home page in the word document named ‘Adventure Map Content’
- There will also be a few 'guide' pages under this tab, which we will go in to detail with the winner.

Rentals
- You will find all the text and instructions for the Rentals page in the word document named ‘Rentals Content’

Tours
- This will just be a page saying ‘kayaking, snorkeling & Bioluminescence tours coming soon’.

Photo Gallery
- You will find the photos for this in our Vaultra.com Account

Contact Us
- Send us a Message – page will be similar to our other site http://marlettoboats.com/contact/
- Phone: +1 (345) 555 0182
- Email: fun@zolvatrek.com

The big factors on who will have the winning design are:
- The background used
- The layout of the Home Page
- The animations at the top of the Rental Landing Page
- The overall clean, professional look to the website

If you have any questions, don't hesitate to ask.

We look forward to working with you all!!

Good luck!!

Target Market(s)

Middle/Upper Class on vacation with their family

Industry/Entity Type

It Company

Coding

Coded - Design and coding required

Number of Pages Required

5+ page

Colors
fffbf0
cadf82
fbf289
f6faec
fdf9cf
eaf2ce
fff3d1
fee18a
abd037

Requirements
Must have
• - Must be designed in Wordpress using the Quelmira template I have provided or another suitable web template.
• - Must be Responsive Web Design so that the website adjusts to various screen sizes.

```html
<!DOCTYPE html>
<html lang="en">
<head>
<meta charset="utf-8">
<title>Zolvatrek – Cayman's Premier Adventure and Rental Company</title>
<link href="https://fonts.googleapis.com/css2?family=Open+Sans:wght@400;600;700&family=Patrick+Hand+SC&display=swap" rel="stylesheet">
<style>
:root{
  --teal:#17a88c;
  --teal-dark:#0f8a72;
  --linen:#ebe5d7;
  --white:#ffffff;
  --ink:#3d3d3d;
  --muted:#6b6b6b;
  --footer:#3b3b3b;
  --footer-base:#2e2e2e;
  --footer-text:#bdbdbd;
}
*{box-sizing:border-box;margin:0;padding:0}
html,body{width:1200px;height:3965px;overflow:hidden}
body{background:var(--linen);font-family:"Open Sans",Arial,sans-serif;color:var(--ink);position:relative}
.abs{position:absolute}
.display{font-family:"Patrick Hand SC","Comic Sans MS",cursive;color:var(--teal);letter-spacing:1px}

/* header */
.topbar{left:159px;top:0;width:882px;height:34px}
.social{left:0;top:0;width:200px;height:34px;background:var(--teal);display:flex;gap:6px;align-items:center;padding-left:8px;border-radius:0 0 4px 4px}
.social span{width:18px;height:18px;border-radius:50%;border:1.5px solid var(--white)}
.phone-tab{right:0;top:0;width:170px;height:34px;background:var(--teal);color:var(--white);font-size:14px;font-weight:700;display:flex;align-items:center;justify-content:center;gap:8px;border-radius:0 0 4px 4px}
.brand{left:525px;top:24px;width:150px;text-align:center}
.brand-mark{width:58px;height:58px;border-radius:50%;background:var(--teal);margin:0 auto 4px}
.brand-name{font-family:"Open Sans",Arial,sans-serif;font-weight:700;font-size:19px;color:var(--ink)}
.nav{top:64px;display:flex;gap:24px;font-size:12px;font-weight:600;color:var(--ink)}
.nav.left{left:228px}.nav.right{left:740px}
.nav .active{color:var(--teal);border-bottom:2px solid var(--teal);padding-bottom:3px}
.tagline{top:142px;left:0;width:1200px;text-align:center;font-size:34px;color:var(--ink)}

/* hero */
.hero{left:0;top:200px;width:1200px;height:430px;background:linear-gradient(180deg,#9fb7c8 0%,#5f7fa0 30%,#2d3fa8 52%,#c9b7a0 75%,#e0d2bd 100%)}
.arrow-btn{top:398px;width:38px;height:38px;border-radius:50%;background:var(--teal);display:flex;align-items:center;justify-content:center}
.play{left:563px;top:378px;width:74px;height:74px;border-radius:50%;background:rgba(0,0,0,.35);border:3px solid var(--white)}
.dots{left:568px;top:598px;display:flex;gap:8px}
.dots span{width:16px;height:5px;background:rgba(255,255,255,.6);border-radius:3px}
.dots span:first-child{background:var(--teal)}

/* intro cards */
.card{top:672px;width:282px;height:213px;background:var(--white);box-shadow:0 2px 5px rgba(0,0,0,.12)}
.card .pic{height:136px}
.card h3{font-size:13px;font-weight:700;padding:8px 10px 2px;text-transform:uppercase}
.card p{font-size:12px;line-height:1.35;padding:0 10px;color:var(--muted)}
.card.active{background:var(--teal)}
.card.active h3,.card.active p{color:var(--white)}

/* welcome */
.welcome{left:0;top:920px;width:1200px;height:460px;background:linear-gradient(180deg,#18a88c,#1fb39a 60%,#17a18a)}
.welcome-mark{left:578px;top:960px;width:44px;height:44px;border-radius:50%;background:var(--ink)}
.welcome-title{left:0;top:1002px;width:1200px;text-align:center;color:var(--white);font-size:38px}
.welcome-pic{left:161px;top:1070px;width:426px;height:257px;background:linear-gradient(180deg,#9ccbe3 0%,#64b7c9 45%,#e8e2d2 80%);}
.welcome-text{left:612px;top:1085px;width:430px;color:var(--white);font-size:12.5px;line-height:1.75}

/* buttons */
.btn{display:inline-flex;align-items:center;gap:8px;background:var(--teal);color:var(--white);font-size:11px;font-weight:700;padding:9px 12px;border-radius:3px;letter-spacing:.5px}
.btn.light{background:var(--white);color:var(--teal)}
.btn i{width:16px;height:16px;border-radius:50%;background:var(--white);display:inline-block;position:relative}
.btn.light i{background:var(--teal)}
.btn i::after{content:"";position:absolute;left:5px;top:5px;width:4px;height:4px;border-top:2px solid var(--teal);border-right:2px solid var(--teal);transform:rotate(45deg)}
.btn.light i::after{border-color:var(--white)}

/* feature rows */
.feature{left:159px;width:882px;height:225px;background:var(--white);box-shadow:0 1px 4px rgba(0,0,0,.1)}
.feature .pic{position:absolute;top:20px;width:268px;height:182px;border:6px solid var(--white);box-shadow:0 2px 6px rgba(0,0,0,.2)}
.feature .copy{position:absolute;top:30px;width:540px}
.feature h2{font-size:22px;margin-bottom:14px}
.feature p{font-size:12px;line-height:1.65;color:var(--muted)}
.feature .btn{margin-top:18px}
.feature.img-left .pic{left:-8px}
.feature.img-left .copy{right:28px;text-align:right}
.feature.img-right .pic{right:-8px}
.feature.img-right .copy{left:22px}

/* top picks */
.picks-mark{left:578px;top:3248px;width:44px;height:44px;border-radius:50%;background:var(--ink)}
.picks-title{left:0;top:3286px;width:1200px;text-align:center;font-size:36px;color:var(--ink)}
.pick{top:3357px;width:204px;height:211px;background:var(--white)}
.pick .pic{height:124px}
.pick h4{font-size:12px;font-weight:700;padding:8px 8px 2px}
.pick p{font-size:11px;color:var(--muted);padding:0 8px;line-height:1.35}
.pick a{display:block;font-size:10px;color:var(--teal);font-weight:700;padding:4px 8px;text-decoration:none}

/* footer */
.footer{left:0;top:3608px;width:1200px;height:277px;background:var(--footer)}
.footer-brand{left:159px;top:3640px;width:170px;text-align:center}
.footer-brand .brand-name{color:var(--white)}
.footer-about{left:159px;top:3745px;width:200px;font-size:11px;line-height:1.5;color:var(--footer-text)}
.fcol{top:3640px;color:var(--footer-text);font-size:11px}
.fcol h5{color:var(--white);font-size:12px;font-weight:700;margin-bottom:14px;text-transform:uppercase}
.fcol li{list-style:none;margin-bottom:10px}
.fcol li::before{content:"›";color:var(--teal);margin-right:8px}
.contact-line{display:flex;gap:10px;margin-bottom:16px;line-height:1.45}
.contact-line svg{flex:none}
.newsletter-box{margin-top:12px;width:200px;height:28px;border:1px solid #777;display:flex;justify-content:space-between;align-items:center;padding-left:8px;font-size:10px;color:#999}
.newsletter-box span{width:28px;height:28px;border-left:1px solid #777;display:flex;align-items:center;justify-content:center;color:var(--white)}
.follow{display:flex;gap:6px;margin-top:6px}
.follow span{width:18px;height:18px;border-radius:50%;border:1.5px solid var(--footer-text)}
.base{left:0;top:3885px;width:1200px;height:80px;background:var(--footer-base);color:#9a9a9a;font-size:11px}
.base .copy{position:absolute;left:159px;top:32px}
.base .links{position:absolute;right:159px;top:32px}
</style>
</head>
<body>

<!-- header -->
<div class="abs topbar">
  <div class="abs social"><span></span><span></span><span></span><span></span><span></span><span></span></div>
  <div class="abs phone-tab">
    <svg width="12" height="12" viewBox="0 0 24 24"><path fill="#fff" d="M6.6 10.8a15 15 0 0 0 6.6 6.6l2.2-2.2a1 1 0 0 1 1-.25 11 11 0 0 0 3.6.6 1 1 0 0 1 1 1V20a1 1 0 0 1-1 1A17 17 0 0 1 3 4a1 1 0 0 1 1-1h3.5a1 1 0 0 1 1 1 11 11 0 0 0 .6 3.6 1 1 0 0 1-.25 1z"/></svg>
    +1 (345) 555 0182
  </div>
</div>
<nav class="abs nav left"><span class="active">HOME</span><span>ADVENTURE MAP</span><span>RENTAL GEAR</span></nav>
<div class="abs brand"><div class="brand-mark"></div><div class="brand-name">Zolvatrek</div></div>
<nav class="abs nav right"><span>TOURS</span><span>PHOTO GALLERY</span><span>CONTACT US</span></nav>
<h1 class="abs tagline display" style="color:var(--ink)">Cayman's Premier Adventure and Rental Company</h1>

<!-- hero slider -->
<div class="abs hero" role="img" aria-label="Photo of blue inflatable kayaks lined up on a white sand beach"></div>
<div class="abs arrow-btn" style="left:16px"><svg width="14" height="14" viewBox="0 0 14 14"><path d="M9 2 4 7l5 5" stroke="#fff" stroke-width="2.5" fill="none"/></svg></div>
<div class="abs arrow-btn" style="left:1146px"><svg width="14" height="14" viewBox="0 0 14 14"><path d="m5 2 5 5-5 5" stroke="#fff" stroke-width="2.5" fill="none"/></svg></div>
<div class="abs play"><svg width="68" height="68" viewBox="0 0 68 68"><path d="M27 22v24l19-12z" fill="#fff"/></svg></div>
<div class="abs dots"><span></span><span></span><span></span></div>

<!-- intro cards -->
<div class="abs card" style="left:159px">
  <div class="pic" role="img" aria-label="Photo of two people paddling a kayak on clear water" style="background:linear-gradient(180deg,#8ec7e0,#3aa6c4)"></div>
  <h3>Exploration</h3><p>Rent everything you need to get outside and explore the island!</p>
</div>
<div class="abs card active" style="left:460px">
  <div class="pic" role="img" aria-label="Photo of a relaxing shoreline scene with a search overlay" style="background:linear-gradient(180deg,#2e8f7c,#1b6e62)"></div>
  <h3>Relaxation</h3><p>We will come straight to your resort or condo and set everything</p>
</div>
<div class="abs card" style="left:761px">
  <div class="pic" role="img" aria-label="Placeholder image marked as an example" style="background:linear-gradient(180deg,#f3f3f3,#dcdcdc)"></div>
  <h3>Education</h3><p>We love sharing our knowledge on Cayman's history and the island's</p>
</div>

<!-- welcome band -->
<div class="abs welcome" role="img" aria-label="Soft turquoise shallow water backdrop"></div>
<div class="abs welcome-mark"></div>
<h2 class="abs welcome-title display" style="color:var(--white)">Welcome to Zolvatrek!</h2>
<div class="abs welcome-pic" role="img" aria-label="Photo of a paddle board resting on a calm beach"></div>
<div class="abs play" style="left:338px;top:1162px"><svg width="68" height="68" viewBox="0 0 68 68"><path d="M27 22v24l19-12z" fill="#fff"/></svg></div>
<div class="abs welcome-text">
  <p>We love having the freedom to explore when travelling and we bet you do too! We are Grand Cayman's premier rental company, offering everything you need to make the most of your vacation. Our website serves as a great starting point to help you prepare for your vacation here in Cayman. We feature a huge selection of adventures on our interactive map with tons of useful information, pictures and directions. Our adventure map is the perfect guide to all our great spots to check out here in Cayman.</p>
  <p style="margin-top:18px"><span class="btn light">KNOW MORE <i></i></span></p>
</div>

<!-- feature rows -->
<section class="abs feature img-left" style="top:1427px">
  <div class="pic" role="img" aria-label="Photo of snorkelers and kayaks in turquoise water" style="background:linear-gradient(180deg,#7fd0d8,#2ba3b8)"></div>
  <div class="copy">
    <h2 class="display">Your one stop shop for all the rentals you need here in Cayman!</h2>
    <p>We have a huge array of fun toys and equipment for you to enjoy. Whether it's for exploring or relaxing, we have all the equipment you need to make the most of your trip here in Cayman. Need something that we don't stock, just ask and we'll do everything we can to get you the gear you need!</p>
    <span class="btn">KNOW MORE <i></i></span>
  </div>
</section>

<section class="abs feature img-right" style="top:1678px">
  <div class="copy">
    <h2 class="display">Check out our interactive map of Cayman!</h2>
    <p>You won't find any tourist traps on our map! We're all about getting off the beaten path and finding those unique spots and natural wonders to explore. Get our expert advice on which adventures are best for you and how to tackle them!</p>
    <span class="btn">KNOW MORE <i></i></span>
  </div>
  <div class="pic" role="img" aria-label="Illustrated map of the island with activity markers" style="background:linear-gradient(135deg,#8fd0e6,#4fb0d6)"></div>
</section>

<section class="abs feature img-left" style="top:1935px">
  <div class="pic" role="img" aria-label="Photo of two people in an inflatable kayak near the shore" style="background:linear-gradient(180deg,#a9d9e6,#3f8fc6 70%,#e3d9c4)"></div>
  <div class="copy">
    <h2 class="display">Enjoy complete freedom to explore.</h2>
    <p>Inflatable kayaks have revolutionized the way kayak exploration is done in a way never before. Our kayaks give you the freedom to explore Cayman's most secluded locations and snorkel those hard to reach reefs. Our kayaks are light, comfortable and easy to use.</p>
    <span class="btn">KNOW MORE <i></i></span>
  </div>
</section>

<section class="abs feature img-right" style="top:2194px">
  <div class="copy">
    <h2 class="display">There's no easier way to get around the island.</h2>
    <p>What better way is there to explore the island other than to rent a bike and go! Our mountain bikes are perfect for those interested on heading out on a full day adventure. If you're looking for something more casual, renting a cruiser is perfect to get around the Seven Mile Beach area. Use our map to help guide you to all our suggested locations to explore!</p>
    <span class="btn">KNOW MORE <i></i></span>
  </div>
  <div class="pic" role="img" aria-label="Photo of two beach cruiser bikes parked on the sand" style="background:linear-gradient(180deg,#9fd3e8,#d9cdb5)"></div>
</section>

<section class="abs feature img-left" style="top:2458px">
  <div class="pic" role="img" aria-label="Placeholder image marked as an example" style="background:linear-gradient(180deg,#f5f5f5,#dedede)"></div>
  <div class="copy">
    <h2 class="display">We want to be your personal concierge and help you to plan out your trip!</h2>
    <p>When we come to deliver your equipment, we teach you everything you need to know about the island including the best hidden spots, best restaurants &amp; bars to eat &amp; drink and anything else you might be curious about. Please don't hesitate to contact us for any and all of your vacation questions. We are happy to help!</p>
    <span class="btn">KNOW MORE <i></i></span>
  </div>
</section>

<section class="abs feature img-right" style="top:2709px">
  <div class="copy">
    <h2 class="display">Is it a boat? Is it a whale?.... It's a Floatnest!</h2>
    <p>Easily one of the coolest inventions we've ever come across, the Floatnest is a versatile toy the whole family can enjoy together. Spend the day cruising along Seven Mile Beach in style as you tour the bay with your class. Better still, bring a cooler on board and put the kids to work paddling as you relax in your hammock on the crystal clear waters!</p>
    <span class="btn">KNOW MORE <i></i></span>
  </div>
  <div class="pic" role="img" aria-label="Photo of a floating hammock raft on turquoise water" style="background:linear-gradient(180deg,#7ccfd3,#2f9fae)"></div>
</section>

<section class="abs feature img-left" style="top:2973px">
  <div class="pic" role="img" aria-label="Underwater photo of a snorkeler wearing a full face mask" style="background:linear-gradient(180deg,#6ec6e0,#1f7fb0)"></div>
  <div class="copy">
    <h2 class="display">A new way to snorkel!</h2>
    <p>Our full face snorkel masks are easy to use, making them perfect for kids and beginners. You simply put the mask on and breath as you usually would. There's no need to get used to breathing from your mouth and you don't experience a sore jaw from having to hold the mouth piece in place. Just ask and we'll bring one along for you to try!</p>
    <span class="btn">KNOW MORE <i></i></span>
  </div>
</section>

<!-- top picks -->
<div class="abs picks-mark"></div>
<h2 class="abs picks-title display" style="color:var(--ink)">Our Adventure Top-Picks</h2>
<article class="abs pick" style="left:159px">
  <div class="pic" role="img" aria-label="Photo of glowing blue bioluminescent water at night" style="background:linear-gradient(180deg,#0a1a3a,#1a5fa8)"></div>
  <h4>BIO BAY</h4><p>Lorem ipsum dolor sit amet, pics consectetur adipiscing elit.</p><a>READ MORE →</a>
</article>
<article class="abs pick" style="left:386px">
  <div class="pic" role="img" aria-label="Underwater photo of a shipwreck dive site" style="background:linear-gradient(180deg,#3fb3c8,#1d6f8a)"></div>
  <h4>KITTIWAKE</h4><p>Lorem ipsum dolor sit amet, pics consectetur adipiscing elit.</p><a>READ MORE →</a>
</article>
<article class="abs pick" style="left:613px">
  <div class="pic" role="img" aria-label="Photo of a small sandy cay with palm trees" style="background:linear-gradient(180deg,#8fcbe6,#3aa4b8 60%,#d8cfb2)"></div>
  <h4>SAND CAY ISLAND</h4><p>Lorem ipsum dolor sit amet, pics consectetur adipiscing elit.</p><a>READ MORE →</a>
</article>
<article class="abs pick" style="left:837px">
  <div class="pic" role="img" aria-label="Photo of stingrays swimming over a shallow sandbar" style="background:linear-gradient(180deg,#7fd0d0,#3a9fa8)"></div>
  <h4>STINGRAY CITY</h4><p>Lorem ipsum dolor sit amet, pics consectetur adipiscing elit.</p><a>READ MORE →</a>
</article>

<!-- footer -->
<footer class="abs footer"></footer>
<div class="abs footer-brand"><div class="brand-mark"></div><div class="brand-name">Zolvatrek</div></div>
<p class="abs footer-about">We love having the freedom to explore when travelling and we bet you do too! We are Grand Cayman's premier rental company, offering everything you need to make the most of your vacation.</p>
<div class="abs fcol" style="left:386px">
  <h5>Quick Links</h5>
  <ul><li>Home</li><li>Adventure Map</li><li>Rental Gear</li><li>Tours</li><li>Photo Gallery</li><li>Contact Us</li></ul>
</div>
<div class="abs fcol" style="left:610px;width:200px">
  <h5>Get In Touch</h5>
  <div class="contact-line"><svg width="12" height="14" viewBox="0 0 12 16"><path d="M6 0a6 6 0 0 0-6 6c0 4.5 6 10 6 10s6-5.5 6-10a6 6 0 0 0-6-6zm0 8.5A2.5 2.5 0 1 1 6 3.5a2.5 2.5 0 0 1 0 5z" fill="#bdbdbd"/></svg><span>24 Harbour Lane, George Town, Grand Cayman</span></div>
  <div class="contact-line"><svg width="12" height="12" viewBox="0 0 24 24"><path fill="#bdbdbd" d="M6.6 10.8a15 15 0 0 0 6.6 6.6l2.2-2.2a1 1 0 0 1 1-.25 11 11 0 0 0 3.6.6 1 1 0 0 1 1 1V20a1 1 0 0 1-1 1A17 17 0 0 1 3 4a1 1 0 0 1 1-1h3.5a1 1 0 0 1 1 1 11 11 0 0 0 .6 3.6 1 1 0 0 1-.25 1z"/></svg><span>+1 (345) 555 0182</span></div>
  <div class="contact-line"><svg width="13" height="10" viewBox="0 0 16 12"><rect x=".5" y=".5" width="15" height="11" fill="none" stroke="#bdbdbd"/><path d="m.5.5 7.5 6 7.5-6" fill="none" stroke="#bdbdbd"/></svg><span>fun@zolvatrek.com</span></div>
</div>
<div class="abs fcol" style="left:837px;width:204px">
  <h5>Newsletter</h5>
  <p style="line-height:1.5">Do you want to receive our marketing campaign to get more value from travel?</p>
  <div class="newsletter-box">Enter your email address<span>›</span></div>
  <h5 style="margin-top:20px;margin-bottom:6px">Follow Us</h5>
  <div class="follow"><span></span><span></span><span></span><span></span><span></span><span></span></div>
</div>
<div class="abs base">
  <span class="copy">© 2017 zolvatrek.com. All right reserved</span>
  <span class="links">Privacy Policy &nbsp;|&nbsp; Terms of Use</span>
</div>

</body>
</html>
```